Bluebird Listings ad 2014 15

I need a design for an advertisement in our Bluebird Listings book telephone directory.
The directory runs for a 12 month period.

Our business offers 24 hour glass replacements to homes, shops and offices.
Our service is usually required by customers that require their glass replaced urgently
.
The ad is 1 of many in the directory offering the same service so we need to attract the customers attention quickly and easily and deliver our message - "24hr glass replacements to doors windows and shopfronts. Call now 9372 4816".

I want to keep the data in the attached ad but with a professional graphic presentation.

The ad size is 58mm high x 83mm wide, full colour.

Target Market(s)

Our customer is generally someone in need of an emergency repair. They aren't spending time shopping around for a product, they have a problem that they want fixed promptly and professionally.

Industry/Entity Type

Business

Font styles to use
Sans Serif

Colors
0255a3
f37022

Requirements
Must have
• "24HR" must stand out, this is a key aspect of our service. The ad needs to be clear and easy to read.

```html
<!DOCTYPE html>
<html lang="en">
<head>
<meta charset="utf-8">
<title>Steadfast Glass – 24hr Glass Replacement</title>
<link rel="stylesheet" href="https://fonts.googleapis.com/css2?family=Anton&family=Bebas+Neue&family=Oswald:wght@400;500;600;700&family=Open+Sans:wght@400;700&family=Ubuntu:wght@400;500;700&display=swap">
<style>
  :root {
    --brand-blue: #0255a3;
    --brand-orange: #f37022;
    --alert-red: #e3221c;
    --ink: #111111;
    --paper: #ffffff;
  }
  * { box-sizing: border-box; margin: 0; padding: 0; }
  html, body { width: 1200px; height: 839px; overflow: hidden; background: var(--paper); }
  .ad {
    position: relative;
    width: 1200px;
    height: 839px;
    background: var(--paper);
    font-family: "Open Sans", sans-serif;
    overflow: hidden;
  }
  .ad p, .ad h1, .ad div, .ad li { white-space: nowrap; }
  .brand-name {
    position: absolute;
    top: 6px; left: 0; width: 1200px;
    text-align: center;
    font-family: "Oswald", sans-serif;
    font-weight: 600;
    font-size: 84px;
    line-height: 1;
    color: var(--brand-blue);
    letter-spacing: 2px;
  }
  .headline {
    position: absolute;
    top: 100px; left: 0; width: 1200px;
    text-align: center;
    font-family: "Bebas Neue", sans-serif;
    font-weight: 400;
    font-size: 205px;
    line-height: 1;
    color: var(--brand-blue);
    letter-spacing: 7px;
  }
  .subhead {
    position: absolute;
    top: 278px; left: 30px;
    font-family: "Anton", sans-serif;
    font-size: 64px;
    line-height: 1;
    color: var(--ink);
    letter-spacing: 2px;
  }
  .call-line {
    position: absolute;
    top: 262px; left: 655px;
    font-family: "Bebas Neue", sans-serif;
    font-size: 100px;
    line-height: 1;
    color: var(--alert-red);
    letter-spacing: 2px;
  }
  .service-panel {
    position: absolute;
    top: 380px; left: 0;
    width: 785px; height: 326px;
    background: var(--brand-blue);
  }
  .checklist {
    position: absolute;
    top: 400px; left: 24px;
    list-style: none;
  }
  .checklist li {
    display: flex;
    align-items: center;
    height: 61px;
    font-size: 31px;
    color: var(--paper);
    letter-spacing: 1.5px;
  }
  .checklist svg { width: 46px; height: 46px; margin-right: 12px; flex: none; }
  .hours-badge {
    position: absolute;
    top: 358px; left: 455px;
    width: 282px; height: 164px;
    background: var(--paper);
    border: 3px solid var(--brand-blue);
    border-radius: 6px;
    display: flex;
    align-items: baseline;
    justify-content: center;
    padding-top: 14px;
    font-family: "Oswald", sans-serif;
    font-weight: 600;
    color: var(--alert-red);
    line-height: 1;
  }
  .hours-badge .num { font-size: 122px; }
  .hours-badge .unit { font-size: 68px; margin-left: 4px; letter-spacing: 2px; }
  .guarantee-badge {
    position: absolute;
    top: 526px; left: 392px;
    width: 226px; height: 182px;
  }
  .guarantee-badge span {
    position: absolute; inset: 0;
    display: flex; align-items: center; justify-content: center;
    text-align: center;
    font-family: "Oswald", sans-serif;
    font-weight: 600;
    font-size: 33px;
    line-height: 1.15;
    color: var(--paper);
  }
  .trade-badge {
    position: absolute;
    top: 517px; left: 610px;
    width: 192px; height: 192px;
    border-radius: 50%;
    background: var(--paper);
    border: 3px solid var(--brand-blue);
    display: flex; align-items: center; justify-content: center;
    text-align: center;
    font-family: "Oswald", sans-serif;
    font-weight: 500;
    font-size: 36px;
    line-height: 1.15;
    color: var(--brand-blue);
  }
  .service-summary {
    position: absolute;
    top: 380px; left: 798px;
    width: 390px;
    font-family: "Ubuntu", sans-serif;
    font-size: 34px;
    line-height: 1.38;
    color: var(--ink);
  }
  .ad .service-summary { white-space: normal; }
  .service-summary .highlight { color: var(--alert-red); }
  .call-now {
    position: absolute;
    top: 532px; left: 798px;
    font-family: "Ubuntu", sans-serif;
    font-weight: 700;
    font-size: 41px;
    letter-spacing: -1px;
    color: var(--ink);
  }
  .call-now .phone { color: var(--alert-red); }
  .insurance-tag {
    position: absolute;
    top: 660px; left: 830px;
    width: 366px; height: 47px;
    background: var(--brand-blue);
    color: var(--paper);
    font-family: "Open Sans", sans-serif;
    font-size: 24px;
    letter-spacing: 1px;
    display: flex; align-items: center; justify-content: center;
  }
  .band {
    position: absolute;
    left: 0; width: 1200px;
    display: flex; align-items: center; justify-content: center;
    font-family: "Oswald", sans-serif;
    font-weight: 600;
    color: var(--paper);
    letter-spacing: 1.5px;
  }
  .band--trust { top: 716px; height: 52px; background: var(--brand-orange); font-size: 38px; }
  .band--promise { top: 778px; height: 61px; background: var(--brand-blue); font-size: 40px; }
</style>
</head>
<body>
<main class="ad">
  <div class="brand-name">steadfast glass</div>
  <h1 class="headline">BROKEN GLASS?</h1>
  <p class="subhead">WE CAN REPLACE IT</p>
  <p class="call-line">CALL 9372 4816</p>

  <section class="service-panel"></section>

  <ul class="checklist">
    <li><svg viewBox="0 0 46 46" aria-hidden="true"><rect x="3" y="9" width="32" height="32" fill="none" stroke="#f37022" stroke-width="4"/><path d="M10 24 L18 33 L40 4" fill="none" stroke="#fff" stroke-width="4" stroke-linecap="round" stroke-linejoin="round"/></svg>DOOR GLASS</li>
    <li><svg viewBox="0 0 46 46" aria-hidden="true"><rect x="3" y="9" width="32" height="32" fill="none" stroke="#f37022" stroke-width="4"/><path d="M10 24 L18 33 L40 4" fill="none" stroke="#fff" stroke-width="4" stroke-linecap="round" stroke-linejoin="round"/></svg>WINDOW GLASS</li>
    <li><svg viewBox="0 0 46 46" aria-hidden="true"><rect x="3" y="9" width="32" height="32" fill="none" stroke="#f37022" stroke-width="4"/><path d="M10 24 L18 33 L40 4" fill="none" stroke="#fff" stroke-width="4" stroke-linecap="round" stroke-linejoin="round"/></svg>SHOWER GLASS</li>
    <li><svg viewBox="0 0 46 46" aria-hidden="true"><rect x="3" y="9" width="32" height="32" fill="none" stroke="#f37022" stroke-width="4"/><path d="M10 24 L18 33 L40 4" fill="none" stroke="#fff" stroke-width="4" stroke-linecap="round" stroke-linejoin="round"/></svg>SHOPFRONT</li>
    <li><svg viewBox="0 0 46 46" aria-hidden="true"><rect x="3" y="9" width="32" height="32" fill="none" stroke="#f37022" stroke-width="4"/><path d="M10 24 L18 33 L40 4" fill="none" stroke="#fff" stroke-width="4" stroke-linecap="round" stroke-linejoin="round"/></svg>STEADFAST GLASS</li>
  </ul>

  <div class="hours-badge"><span class="num">24</span><span class="unit">HR</span></div>

  <div class="guarantee-badge">
    <svg viewBox="0 0 226 182" width="226" height="182" aria-hidden="true">
      <g fill="#f37022">
        <circle cx="60" cy="50" r="40"/>
        <circle cx="113" cy="38" r="36"/>
        <circle cx="166" cy="50" r="40"/>
        <circle cx="40" cy="95" r="38"/>
        <circle cx="186" cy="95" r="38"/>
        <circle cx="62" cy="138" r="40"/>
        <circle cx="113" cy="148" r="34"/>
        <circle cx="164" cy="138" r="40"/>
        <ellipse cx="113" cy="92" rx="90" ry="62"/>
      </g>
    </svg>
    <span>ALL WORK<br>GUARANTEED</span>
  </div>

  <div class="trade-badge">QUALIFIED<br>TRADESMEN</div>

  <p class="service-summary"><span class="highlight">24hr</span> glass replacements to doors windows and shopfronts.</p>
  <p class="call-now">Call now <span class="phone">9372 4816</span></p>

  <div class="insurance-tag">INSURANCE BILLED DIRECT</div>

  <div class="band band--trust">THE TRUSTED NAME IN GLASS REPLACEMENT</div>
  <div class="band band--promise">REGAIN THE SAFETY AND SECURITY IN YOUR HOME, SHOP OR OFFICE</div>
</main>
</body>
</html>
```